brevity cafe flyer design project

A funky trendy cafe in Melbourne’s CBD that caters too a large range of corporate clients. Located on the door step of a major train station, its a quick turn around cafe for the short time frame customer but also a cafe to sit, relax and enjoy the hustle and bustle from the inside out. We provide All day breakfast, gourmet sandwiches, gourmet rotti wraps, a la carte menu and also heat and serve meals.

BREAKFAST TO GO! ALL BREAKFAST TO GO ITEMS COME WITH A MEDIUM TAKE AWAY COFFEE!
• RAISIN TOAST & COFFEE – $6
• BACON & EGG MUFFIN & COFFEE $7.5
• SPINACH, MUSHROOM OMELETTE MUFFIN & COFFEE $7.5
• OMELETTE WITH CHEESE MUFFIN & COFFEE $7.5
• HAM & CHEESE CROISSANT & COFFEE $7.5
• SWEET OR SAVOURY MUFFIN & COFFEE $6.5
• HAM & CHEESE SANDWICH & COFFEE $8.0
• HAM, CHEESE & TOMATO SANDWICH & COFFEE $8.5

*NOT IN CONJUNCTION WITH BREVITY CLUB CARD OFFER

WE ALSO HAVE PRE-MADE LUNCH OPTIONS – ASSORTED ROTTI WRAPS (Bbq chicken, honey mustard chicken, pesto chicken & vegetarian) ASSORTED GOURMET SANDWICHES (Mediterranean, Moroccan chicken, Salami, Chicken Schnitzel, Salmon, Brevity & Roast Beef) Soup of the day Pasta of the day Salad of the day

Ph- 03 9718 4630 Fax- 03 9718 4637 Web – www.brevitycafe.com.au 182 DORNAL STREET MELBOURNE 3000

Industry/Entity Type

Cafe

Font styles to use
Serif

Requirements
Must have
• Our 2 branded colours -

PMS 392c
PMS BLACK

```html
<!DOCTYPE html>
<html lang="en">
<head>
<meta charset="utf-8">
<title>Brevity Cafe – Breakfast To Go</title>
<link rel="stylesheet" href="https://fonts.googleapis.com/css2?family=Montserrat:wght@600;700;800&family=Questrial&display=swap">
<style>
  :root {
    --lime: #cbe23b;
    --black: #000000;
    --stage: #0b1a3a;
    --green-photo-a: #a9c62c;
    --green-photo-b: #4e6410;
    --pink-photo-a: #d23aa8;
    --pink-photo-b: #4a0c3a;
  }
  * { margin: 0; padding: 0; box-sizing: border-box; }
  html, body {
    width: 1200px; height: 2226px; overflow: hidden;
    background: var(--stage);
  }
  .flyer {
    position: absolute; left: 75px; top: 32px;
    width: 1050px; height: 2162px;
    background: var(--black); color: var(--lime);
    font-family: "Questrial", "Century Gothic", sans-serif;
  }
  .brand { position: absolute; left: 0; right: 0; text-align: center; }
  .brand-mark {
    position: absolute; left: 50%; top: 70px; width: 120px; height: 120px;
    margin-left: -60px; border-radius: 50%; background: var(--lime);
  }
  .brand-name {
    top: 360px; font-family: "Questrial", sans-serif;
    font-size: 62px; letter-spacing: 6px; color: var(--lime);
  }
  .headline {
    position: absolute; left: 66px; top: 500px; width: 940px;
    font-family: "Montserrat", sans-serif; font-weight: 800;
    font-size: 28px; line-height: 36px; text-transform: uppercase;
  }
  .menu { position: absolute; left: 66px; top: 600px; width: 920px; list-style: none; }
  .menu-item {
    display: flex; align-items: center; height: 61px;
    font-size: 31px;
  }
  .menu-item svg { width: 36px; height: 30px; margin-right: 18px; flex: none; }
  .menu-item .dish { flex: 1; }
  .menu-item .price { width: 78px; text-align: left; }
  .note {
    position: absolute; left: 66px; top: 1100px;
    font-size: 22px; color: var(--lime); letter-spacing: 0.3px;
  }
  .photos { position: absolute; left: 0; top: 1159px; width: 1050px; height: 432px; display: flex; }
  .photo-green { width: 585px; height: 100%; background: linear-gradient(135deg, var(--green-photo-a), var(--green-photo-b)); }
  .photo-pink { width: 465px; height: 100%; background: linear-gradient(135deg, var(--pink-photo-a), var(--pink-photo-b)); }
  .lunch {
    position: absolute; left: 0; right: 0; top: 1625px;
    text-align: center; font-size: 29px; line-height: 42px;
  }
  .lunch .lunch-heading {
    font-family: "Montserrat", sans-serif; font-weight: 700; font-size: 29px;
  }
  .lunch .gap { margin-top: 18px; }
  .lunch .daily { margin-top: 14px; font-family: "Montserrat", sans-serif; font-weight: 700; }
  .contact {
    position: absolute; left: 0; top: 1983px; width: 1050px; height: 179px;
    background: var(--lime); color: var(--black);
    font-family: "Montserrat", sans-serif; font-weight: 700; font-size: 34px;
    text-align: center; padding-top: 14px;
  }
  .contact-line { display: flex; justify-content: center; align-items: center; height: 52px; gap: 10px; }
  .contact-line svg { width: 30px; height: 30px; flex: none; }
  .contact-line .spacer { width: 14px; }
</style>
</head>
<body>
<main class="flyer">
  <div class="brand-mark"></div>
  <div class="brand brand-name">BREVITY CAFE</div>

  <h1 class="headline">Breakfast to go! All breakfast to go items<br>come with a medium take away coffee!</h1>

  <ul class="menu">
    <li class="menu-item"><svg viewBox="0 0 36 30"><path d="M4 12h22v6a9 9 0 0 1-9 9h-4a9 9 0 0 1-9-9z M26 14h4a4 4 0 0 1 0 8h-4" fill="#cbe23b"/><path d="M12 2c-3 3 3 4 0 8M18 2c-3 3 3 4 0 8" stroke="#cbe23b" stroke-width="2" fill="none"/></svg><span class="dish">Raisin Toast &amp; Coffee</span><span class="price">$6</span></li>
    <li class="menu-item"><svg viewBox="0 0 36 30"><path d="M4 12h22v6a9 9 0 0 1-9 9h-4a9 9 0 0 1-9-9z M26 14h4a4 4 0 0 1 0 8h-4" fill="#cbe23b"/><path d="M12 2c-3 3 3 4 0 8M18 2c-3 3 3 4 0 8" stroke="#cbe23b" stroke-width="2" fill="none"/></svg><span class="dish">Bacon &amp; Egg Muffin &amp; Coffee</span><span class="price">$7.5</span></li>
    <li class="menu-item"><svg viewBox="0 0 36 30"><path d="M4 12h22v6a9 9 0 0 1-9 9h-4a9 9 0 0 1-9-9z M26 14h4a4 4 0 0 1 0 8h-4" fill="#cbe23b"/><path d="M12 2c-3 3 3 4 0 8M18 2c-3 3 3 4 0 8" stroke="#cbe23b" stroke-width="2" fill="none"/></svg><span class="dish">Spinach, Mushroom Omelette Muffin &amp; Coffee</span><span class="price">$7.5</span></li>
    <li class="menu-item"><svg viewBox="0 0 36 30"><path d="M4 12h22v6a9 9 0 0 1-9 9h-4a9 9 0 0 1-9-9z M26 14h4a4 4 0 0 1 0 8h-4" fill="#cbe23b"/><path d="M12 2c-3 3 3 4 0 8M18 2c-3 3 3 4 0 8" stroke="#cbe23b" stroke-width="2" fill="none"/></svg><span class="dish">Omelette with Cheese Muffin &amp; Coffee</span><span class="price">$7.5</span></li>
    <li class="menu-item"><svg viewBox="0 0 36 30"><path d="M4 12h22v6a9 9 0 0 1-9 9h-4a9 9 0 0 1-9-9z M26 14h4a4 4 0 0 1 0 8h-4" fill="#cbe23b"/><path d="M12 2c-3 3 3 4 0 8M18 2c-3 3 3 4 0 8" stroke="#cbe23b" stroke-width="2" fill="none"/></svg><span class="dish">Ham &amp; Cheese Croissant &amp; Coffee</span><span class="price">$7.5</span></li>
    <li class="menu-item"><svg viewBox="0 0 36 30"><path d="M4 12h22v6a9 9 0 0 1-9 9h-4a9 9 0 0 1-9-9z M26 14h4a4 4 0 0 1 0 8h-4" fill="#cbe23b"/><path d="M12 2c-3 3 3 4 0 8M18 2c-3 3 3 4 0 8" stroke="#cbe23b" stroke-width="2" fill="none"/></svg><span class="dish">Sweet or Savoury Muffin &amp; Coffee</span><span class="price">$6.5</span></li>
    <li class="menu-item"><svg viewBox="0 0 36 30"><path d="M4 12h22v6a9 9 0 0 1-9 9h-4a9 9 0 0 1-9-9z M26 14h4a4 4 0 0 1 0 8h-4" fill="#cbe23b"/><path d="M12 2c-3 3 3 4 0 8M18 2c-3 3 3 4 0 8" stroke="#cbe23b" stroke-width="2" fill="none"/></svg><span class="dish">Ham &amp; Cheese Sandwich &amp; Coffee</span><span class="price">$8.0</span></li>
    <li class="menu-item"><svg viewBox="0 0 36 30"><path d="M4 12h22v6a9 9 0 0 1-9 9h-4a9 9 0 0 1-9-9z M26 14h4a4 4 0 0 1 0 8h-4" fill="#cbe23b"/><path d="M12 2c-3 3 3 4 0 8M18 2c-3 3 3 4 0 8" stroke="#cbe23b" stroke-width="2" fill="none"/></svg><span class="dish">Ham, Cheese &amp; Tomato Sandwich &amp; Coffee</span><span class="price">$8.5</span></li>
  </ul>

  <p class="note">*NOT IN CONJUNCTION WITH BREVITY CLUB CARD OFFER</p>

  <section class="photos">
    <div class="photo-green" role="img" aria-label="Cafe interior with long bench seating and tables, tinted lime green"></div>
    <div class="photo-pink" role="img" aria-label="Cafe dining area with rows of tables and chairs, tinted magenta"></div>
  </section>

  <section class="lunch">
    <p class="lunch-heading">WE ALSO HAVE PRE-MADE LUNCH OPTIONS –</p>
    <p>ASSORTED ROTTI WRAPS (Bbq chicken, honey mustard chicken,</p>
    <p>pesto chicken &amp; vegetarian)</p>
    <p class="lunch-heading gap">ASSORTED GOURMET SANDWICHES</p>
    <p>(Mediterranean, Moroccan chicken, Salami, Chicken Schnitzel,</p>
    <p>Salmon, Brevity &amp; Roast Beef)</p>
    <p class="daily">Soup of the day Pasta of the day Salad of the day</p>
  </section>

  <footer class="contact">
    <div class="contact-line">
      <svg viewBox="0 0 30 30"><circle cx="15" cy="15" r="14" fill="#000"/><path d="M10 8l3 0 1 4-2 1.5a9 9 0 0 0 4 4l1.5-2 4 1 0 3a2 2 0 0 1-2 2A13 13 0 0 1 8 10a2 2 0 0 1 2-2z" fill="#cbe23b"/></svg>
      <span>03 9718 4630</span><span class="spacer"></span>
      <svg viewBox="0 0 30 30"><circle cx="15" cy="15" r="14" fill="#000"/><rect x="9" y="9" width="12" height="12" rx="1" fill="#cbe23b"/><rect x="11" y="11" width="8" height="3" fill="#000"/></svg>
      <span>03 9718 4637</span>
    </div>
    <div class="contact-line">
      <svg viewBox="0 0 30 30"><circle cx="15" cy="15" r="14" fill="#000"/><circle cx="15" cy="15" r="8" fill="none" stroke="#cbe23b" stroke-width="2"/><path d="M7 15h16M15 7c-4 5-4 11 0 16M15 7c4 5 4 11 0 16" stroke="#cbe23b" stroke-width="1.6" fill="none"/></svg>
      <span>www.brevitycafe.com.au</span>
    </div>
    <div class="contact-line">
      <svg viewBox="0 0 30 30"><path d="M15 2a9 9 0 0 1 9 9c0 7-9 17-9 17S6 18 6 11a9 9 0 0 1 9-9z" fill="#000"/><circle cx="15" cy="11" r="3.5" fill="#cbe23b"/></svg>
      <span>182 DORNAL STREET MELBOURNE 3000</span>
    </div>
  </footer>
</main>
</body>
</html>
```